Tamrock Stationery Design Project

company name : Tamrock General Trading LLC.
light watermark taken from the logo to cover almost the middle of the stationary..
logo is attached and an on going business card project is released on the same company name..
thanks
Reason: more time for more designs and to work with comfort..
Industry/Entity Type
Business
Colors
Designer to choose colors to be used in the design.
Look and feel
Each slider illustrates characteristics of the customer's brand and the style your logo design should communicate.

```html
<!DOCTYPE html>
<html lang="en">
<head>
<meta charset="utf-8">
<title>Corveth Stationery</title>
<link href="https://fonts.googleapis.com/css2?family=Cinzel:wght@500&family=Crimson+Pro:wght@400;600;700&display=swap" rel="stylesheet">
<style>
  :root {
    --backdrop: #e7e4df;
    --paper: #ffffff;
    --ink: #2e2e2e;
    --ink-soft: #555555;
    --brand-blue: #1a7fc1;
    --brand-deep: #0f5595;
    --brand-grey: #4a4a4a;
    --mark-grey: #efefef;
    --mark-blue: #e6f0f8;
  }
  * { margin: 0; padding: 0; box-sizing: border-box; }
  html, body { width: 1029px; height: 1200px; overflow: hidden; }
  body {
    position: relative;
    background: var(--backdrop);
    font-family: "Crimson Pro", Georgia, serif;
    color: var(--ink);
  }
  .sheet {
    position: absolute;
    background: var(--paper);
    box-shadow: 0 2px 8px rgba(0,0,0,.18);
    overflow: hidden;
  }
  .brand-name {
    position: relative;
    z-index: 2;
    font-family: "Cinzel", "Times New Roman", serif;
    font-weight: 500;
    color: var(--brand-grey);
    letter-spacing: .02em;
    white-space: nowrap;
  }
  .watermark {
    position: absolute;
    z-index: 0;
    background: linear-gradient(160deg, transparent 20%, var(--mark-grey) 50%, var(--mark-blue) 70%, transparent 90%);
    border-radius: 50%;
    opacity: .75;
  }
  .contact-icon {
    display: inline-block;
    width: 8px; height: 8px;
    border-radius: 50%;
    background: var(--brand-blue);
    margin-right: 3px;
    vertical-align: -0.5px;
  }

  /* Envelope front */
  .envelope-front { left: 62px; top: 50px; width: 535px; height: 238px; }
  .envelope-front .brand-name { position: absolute; left: 18px; top: 48px; font-size: 14px; }
  .envelope-front .return-address { position: absolute; left: 18px; top: 68px; font-size: 9px; line-height: 11px; }
  .envelope-front .watermark { left: 270px; top: 105px; width: 260px; height: 150px; }

  /* Envelope back */
  .envelope-back { left: 62px; top: 300px; width: 535px; height: 160px; }
  .envelope-back .flap {
    position: absolute; left: 0; top: 0; width: 535px; height: 79px;
    background: linear-gradient(90deg, #169bd4 0%, #1383c4 50%, var(--brand-deep) 100%);
    border-radius: 0 0 14px 14px;
  }
  .envelope-back .brand-name { position: absolute; left: 0; right: 0; top: 44px; text-align: center; color: #fff; font-size: 12px; }

  /* Business cards */
  .card-back { left: 692px; top: 195px; width: 235px; height: 148px; z-index: 1; }
  .card-back .brand-name { position: absolute; left: 27px; top: 72px; font-size: 13px; }
  .card-back .watermark { left: 60px; top: 20px; width: 190px; height: 140px; }
  .card-front { left: 646px; top: 90px; width: 237px; height: 135px; z-index: 2; }
  .card-front .brand-name { position: absolute; left: 32px; top: 38px; font-size: 12px; }
  .card-front .holder { position: absolute; left: 32px; top: 68px; font-size: 8px; font-weight: 700; color: var(--brand-blue); letter-spacing: .03em; }
  .card-front .role { position: absolute; left: 32px; top: 78px; font-size: 5.5px; color: var(--ink-soft); }
  .card-front .rule { position: absolute; left: 32px; top: 85px; width: 175px; height: 1px; background: #ddd; }
  .card-front .lines { position: absolute; left: 32px; top: 93px; font-size: 6.5px; line-height: 8.5px; }
  .card-front .lines .contact-icon { width: 6px; height: 6px; }
  .card-front .address { position: absolute; left: 129px; top: 94px; font-size: 5.5px; line-height: 7.5px; }

  /* Letterheads */
  .letter-blank { left: 26px; top: 450px; width: 520px; height: 735px; z-index: 1; }
  .letter-blank .brand-name { position: absolute; left: 48px; top: 80px; font-size: 19px; }
  .letter-blank .watermark { left: 240px; top: 430px; width: 300px; height: 260px; }
  .letter-full { left: 459px; top: 394px; width: 508px; height: 718px; z-index: 2; }
  .letter-full .brand-name { position: absolute; left: 40px; top: 66px; font-size: 19px; }
  .letter-full .watermark { left: 120px; top: 510px; width: 400px; height: 200px; }

  .letter-date { position: absolute; right: 40px; top: 132px; font-size: 11.5px; }
  .recipient { position: absolute; left: 40px; top: 144px; font-size: 11.5px; line-height: 13px; }
  .recipient strong { font-weight: 700; }
  .letter-body { position: absolute; left: 40px; top: 196px; width: 428px; font-size: 10.6px; line-height: 15.4px; text-align: justify; }
  .letter-body p + p { margin-top: 15.4px; }
  .sign-off { position: absolute; z-index: 2; left: 40px; top: 520px; font-size: 11px; line-height: 14px; }
  .signature { width: 130px; height: 30px; background: rgba(60,60,60,.08); border-radius: 4px; margin: 2px 0; }

  .letter-footer { position: absolute; z-index: 2; left: 40px; bottom: 30px; font-size: 9px; line-height: 11px; white-space: nowrap; }
  .letter-blank .letter-footer { left: 118px; }
  .letter-footer .company { color: var(--brand-blue); font-weight: 600; }
  .letter-footer .contact-icon { margin-left: 6px; }
  .letter-footer .contact-icon:first-child { margin-left: 0; }
</style>
</head>
<body>

  <section class="sheet envelope-front">
    <div class="watermark" role="img" aria-label="faint brand watermark"></div>
    <div class="brand-name">Corveth Int.</div>
    <div class="return-address">42 Harbour Lane,<br>P.O. Box 210, Eastvale,<br>B.C. V3K 1R8</div>
  </section>

  <section class="sheet envelope-back">
    <div class="flap"><div class="brand-name">Corveth Int.</div></div>
  </section>

  <section class="sheet card-back">
    <div class="watermark" role="img" aria-label="faint brand watermark"></div>
    <div class="brand-name">Corveth Int.</div>
  </section>

  <section class="sheet card-front">
    <div class="brand-name">Corveth Int.</div>
    <div class="holder">ALEX MARLOWE</div>
    <div class="role">General Manager</div>
    <div class="rule"></div>
    <div class="lines">
      <span class="contact-icon"></span>55.204.7731<br>
      <span class="contact-icon"></span>55.318.9062<br>
      <span class="contact-icon"></span>info@corvethint.com
    </div>
    <div class="address">42 Harbour Lane,<br>P.O. Box 210, Eastvale,<br>B.C. V3K 1R8</div>
  </section>

  <section class="sheet letter-blank">
    <div class="watermark" role="img" aria-label="faint brand watermark"></div>
    <div class="brand-name">Corveth Int.</div>
    <div class="letter-footer">
      <div class="company">Corveth General Trading LLC.</div>
      <div>42 Harbour Lane, P.O. Box 210, Eastvale, B.C. V3K 1R8</div>
      <div><span class="contact-icon"></span>55.204.7731 <span class="contact-icon"></span>55.318.9062 <span class="contact-icon"></span>info@corvethint.com <span class="contact-icon"></span>www.corvethint.com</div>
    </div>
  </section>

  <section class="sheet letter-full">
    <div class="watermark" role="img" aria-label="faint brand watermark"></div>
    <div class="brand-name">Corveth Int.</div>
    <div class="letter-date">October 30, 2014</div>
    <div class="recipient"><strong>Daniel Reyes</strong><br>General Manager<br>Northgate Holdings</div>
    <div class="letter-body">
      <p>Lorem ipsum dolor sit amet, consectetur adipiscing elit. Donec orci purus, luctus vitae dignissim eu, iaculis sed purus. Vivamus faucibus, ipsum nec aliquet viverra, leo mauris condimentum ligula, sit amet sagittis enim ligula quis arcu. Nam egestas tortor id nisi porttitor mattis. In tortor ante, ultricies in suscipit a, tempus non massa.</p>
      <p>Quisque scelerisque sagittis nulla at porttitor. Mauris a justo et tellus interdum tristique. Sed id augue vitae urna euismod commodo aliquet a quam. Pellentesque arcu velit, cursus et malesuada ut, rutrum nisi iaculis consequat et diam. Nullam erat sem, rhoncus id ullamcorper vitae, rhoncus et arcu. In ultricies ultricies nulla, ut rutrum nisi iaculis at. Donec eu magna a metus ornare faucibus. Fusce aliquet faucibus ultricies. Morbi semper, est id tincidunt gravida, sem arcu adipiscing lacus, ac bibendum nulla leo eu purus. Quisque nec diam sed risus consectetur a accumsan quis quis nibh. Vestibulum id purus lorem.</p>
      <p>Vivamus et auctor mi. Fusce vel massa nulla. Phasellus nec eros mauris, et scelerisque orci. Donec malesuada orci vitae nulla accumsan porta a id massa. Quisque accumsan iaculis magna sit amet fringilla. Maecenas consequat, magna eget tincidunt semper, odio nibh rutrum mi, id feugiat ante nisi eu risus. Vestibulum nunc orci, ultricies in mi. Quisque scelerisque sagittis nulla at porttitor. Mauris a justo et tellus interdum tristique. Sed id augue vitae urna euismod commodo lorem ipsum aliquet a quam.</p>
    </div>
    <div class="sign-off">
      Keep moving forward!
      <div class="signature" role="img" aria-label="handwritten signature"></div>
      Alex Marlowe
    </div>
    <div class="letter-footer">
      <div class="company">Corveth General Trading LLC.</div>
      <div>42 Harbour Lane, P.O. Box 210, Eastvale, B.C. V3K 1R8</div>
      <div><span class="contact-icon"></span>55.204.7731 <span class="contact-icon"></span>55.318.9062 <span class="contact-icon"></span>info@corvethint.com <span class="contact-icon"></span>www.corvethint.com</div>
    </div>
  </section>

</body>
</html>
```